Business Cards

Simple but professional looking business cards

Name: Rina Tolvardi
Title: Principle Horizon Applications Consultant
Email: r@kbrx.net.au
web : www.kbrx.net.au
Phone: +61.8.95203417
Mobile: +61.431862055
Updates

Hi All, Please include the office address Level 1, 200 Quarrington St, Kelverton, KR, 4410

Industry/Entity Type

Business

```html
<!DOCTYPE html>
<html lang="en">
<head>
<meta charset="utf-8">
<title>KBRX Business Cards</title>
<link href="https://fonts.googleapis.com/css2?family=Lato:wght@400;700&display=swap" rel="stylesheet">
<style>
  :root {
    --backdrop: #3b3b3b;
    --card: #ffffff;
    --brand-blue: #1b5fb0;
    --brand-green: #7dc242;
    --ink: #4a4a4a;
    --ink-dark: #2f2f2f;
    --badge-red: #e3201b;
  }
  html, body {
    margin: 0;
    padding: 0;
    width: 1200px;
    height: 1000px;
    overflow: hidden;
    background: var(--backdrop);
    font-family: "Lato", Arial, sans-serif;
  }
  .stage {
    position: relative;
    width: 1200px;
    height: 1000px;
  }
  .card {
    position: absolute;
    width: 599px;
    height: 346px;
    background: var(--card);
    box-shadow: 0 6px 14px rgba(0,0,0,0.45);
  }
  .card--front { left: 176px; top: 132px; }
  .card--back  { left: 443px; top: 533px; }

  .wordmark {
    position: absolute;
    left: 0;
    right: 0;
    top: 135px;
    text-align: center;
    font-size: 72px;
    font-weight: 700;
    letter-spacing: 2px;
    line-height: 1;
    color: var(--brand-blue);
  }

  .identity {
    position: absolute;
    left: 60px;
    top: 172px;
    width: 220px;
    text-align: center;
  }
  .identity__name {
    margin: 0;
    font-size: 19px;
    font-weight: 700;
    color: var(--brand-green);
    line-height: 1.2;
  }
  .identity__title {
    margin: 3px 0 0;
    font-size: 14px;
    color: var(--ink-dark);
    line-height: 1.4;
  }

  .address {
    position: absolute;
    left: 360px;
    top: 52px;
    margin: 0;
    font-size: 14.5px;
    font-weight: 400;
    color: var(--ink-dark);
    line-height: 1.5;
    font-style: normal;
  }
  .contacts {
    position: absolute;
    left: 360px;
    top: 133px;
    margin: 0;
    padding: 0;
    list-style: none;
  }
  .contacts__item {
    display: flex;
    align-items: center;
    height: 22px;
    font-size: 14px;
    font-weight: 400;
    color: var(--ink-dark);
  }
  .contacts__icon {
    width: 16px;
    height: 16px;
    margin-right: 8px;
    fill: var(--brand-green);
  }

  .partner {
    position: absolute;
    left: 360px;
    top: 274px;
    display: flex;
    align-items: center;
  }
  .partner__badge {
    width: 128px;
    height: 27px;
    background: var(--badge-red);
  }
  .partner__label {
    margin-left: 10px;
    font-size: 14px;
    font-weight: 700;
    color: var(--ink-dark);
    line-height: 1.25;
  }
</style>
</head>
<body>
<main class="stage">
  <section class="card card--front" aria-label="Business card front">
    <div class="wordmark">KBRX</div>
  </section>

  <section class="card card--back" aria-label="Business card back">
    <div class="identity">
      <p class="identity__name">Rina Tolvardi</p>
      <p class="identity__title">Principle Horizon<br>Applications Consultant</p>
    </div>

    <address class="address">Level 1, 200 Quarrington St,<br>Kelverton, KR, 4410</address>

    <ul class="contacts">
      <li class="contacts__item">
        <svg class="contacts__icon" viewBox="0 0 24 24" aria-hidden="true"><path d="M6.6 10.8a15.1 15.1 0 0 0 6.6 6.6l2.2-2.2a1 1 0 0 1 1-.25 11.4 11.4 0 0 0 3.6.57 1 1 0 0 1 1 1V20a1 1 0 0 1-1 1A17 17 0 0 1 3 4a1 1 0 0 1 1-1h3.5a1 1 0 0 1 1 1c0 1.250.2 2.450.57 3.57a1 1 0 0 1-.25 1z"/></svg>
        +61.8.95203417
      </li>
      <li class="contacts__item">
        <svg class="contacts__icon" viewBox="0 0 24 24" aria-hidden="true"><path d="M7 1h10a2 2 0 0 1 2 2v18a2 2 0 0 1-2 2H7a2 2 0 0 1-2-2V3a2 2 0 0 1 2-2zm0 3v14h10V4zm5 15.5a1 1 0 1 0 0 2 1 1 0 0 0 0-2z"/></svg>
        +61.431862055
      </li>
      <li class="contacts__item">
        <svg class="contacts__icon" viewBox="0 0 24 24" aria-hidden="true"><path d="M2 5h20v2l-10 6L2 7zm0 4.3l10 6 10-6V19H2z"/></svg>
        r@kbrx.net.au
      </li>
      <li class="contacts__item">
        <svg class="contacts__icon" viewBox="0 0 24 24" aria-hidden="true"><path d="M12 2a10 10 0 1 0 0 20 10 10 0 0 0 0-20zm-1 17.9A8 8 0 0 1 4.2 10.6L9 15v1a2 2 0 0 0 2 2zm6.9-2.5A2 2 0 0 0 16 16h-1v-3a1 1 0 0 0-1-1H8v-2h2a1 1 0 0 0 1-1V7h2a2 2 0 0 0 2-2v-.4a8 8 0 0 1 2.9 12.8z"/></svg>
        www.kbrx.net.au
      </li>
    </ul>

    <div class="partner">
      <div class="partner__badge" role="img" aria-label="Partner badge"></div>
      <div class="partner__label">Gold<br>Partner</div>
    </div>
  </section>
</main>
</body>
</html>
```